Zelno Vigor Iron Tempo Multi Vitamin Label Design

We need a label design for our Sports Performance Daily Multi Vitamin specially created and branded for our Zelno Vigor line for the University of Calvoria. The feel is edgy, sports nutrition. Two logos need to be incorporated... Zelno and the Collective Logo attached. The colors should be the official colors of the University of Calvoria. The font may also be the Georgia font... or the Zelno font. Or any font. A hydration product will also be created later on...so this label design may be used on many products. Please utilize the collective logo similar to the use in the attached photo. No official trademark items from the University of Calvoria should be used. Attached is also an image if the bottle (white) that will be used for the vitamin. Please use red, black, grey, white. We are looking for the front design only right now and once selected, will work on the nutrition/back label portion with the artist.

```html
<!DOCTYPE html>
<html lang="en">
<head>
<meta charset="utf-8">
<title>Zelno Vigor Daily Multi Vitamin Label</title>
<link rel="stylesheet" href="https://fonts.googleapis.com/css2?family=Tinos&family=Exo+2:ital,wght@1,800&display=swap">
<style>
  :root {
    --backdrop: #d8d8d8;
    --label-white: #ffffff;
    --brand-red: #c42f3e;
    --brand-red-deep: #a81f2d;
    --panel-grey: #a9a9a9;
    --ink-black: #1e1e1e;
  }
  * { margin: 0; padding: 0; box-sizing: border-box; }
  html, body {
    width: 1200px;
    height: 1185px;
    overflow: hidden;
    background: var(--backdrop);
  }
  .canvas {
    position: relative;
    width: 1200px;
    height: 1185px;
  }
  .label {
    position: absolute;
    left: 290px;
    top: 150px;
    width: 620px;
    height: 885px;
    background: var(--label-white);
    overflow: hidden;
  }
  .brand-mark {
    position: absolute;
    top: 105px;
    left: 0;
    width: 100%;
    text-align: center;
    font-family: "Tinos", Georgia, serif;
    font-size: 118px;
    line-height: 1;
    color: var(--brand-red);
    letter-spacing: 2px;
  }
  .product-band {
    position: absolute;
    left: 0;
    top: 330px;
    width: 100%;
    height: 555px;
    background: linear-gradient(90deg, var(--brand-red-deep) 0%, var(--brand-red) 18%, var(--brand-red) 80%, var(--brand-red-deep) 100%);
    border-top-right-radius: 70px;
  }
  .product-title {
    position: absolute;
    left: 70px;
    top: 50px;
    color: var(--label-white);
  }
  .product-title .daily {
    display: block;
    font-family: "Tinos", Georgia, serif;
    font-size: 72px;
    line-height: 1;
    letter-spacing: 1px;
  }
  .product-title .name {
    display: block;
    font-family: "Exo 2", Arial, sans-serif;
    font-weight: 800;
    font-style: italic;
    font-size: 82px;
    line-height: 0.98;
    margin-top: 14px;
  }
  .partner-panel {
    position: absolute;
    left: 0;
    bottom: 0;
    width: 100%;
    height: 140px;
  }
  .partner-badge {
    position: absolute;
    left: 0;
    bottom: 0;
    width: 450px;
    height: 140px;
    background: var(--label-white);
    border-top-right-radius: 28px;
    display: flex;
    align-items: center;
    justify-content: center;
    font-family: "Tinos", Georgia, serif;
    font-size: 36px;
    color: var(--ink-black);
  }
  .partner-side {
    position: absolute;
    left: 470px;
    bottom: 0;
    width: 150px;
    height: 140px;
    background: linear-gradient(180deg, var(--panel-grey), #8e8e8e);
    border-top-left-radius: 28px;
  }
</style>
</head>
<body>
  <div class="canvas">
    <div class="label">
      <div class="brand-mark">Zelno</div>
      <div class="product-band">
        <h1 class="product-title">
          <span class="daily">DAILY</span>
          <span class="name">Multi<br>Vitamin</span>
        </h1>
        <div class="partner-panel">
          <div class="partner-badge">Civic Row Collective</div>
          <div class="partner-side"></div>
        </div>
      </div>
    </div>
  </div>
</body>
</html>
```